Presentation Folder and Inserts for Scientific Recruiting Firm

Harborline Staffing is a Pharmaceutical and Biotech recruiting firm. We help companies locate ideal candidates to fill positions within their companies. We want to have presentation materials designed to be handed out to clients at career fairs.

 

WE ARE OPEN TO ALL TYPES OF DESIGNS. 

 

We will have the need for the design of many more projects in the coming months.  We would love to find a great designer to work with on all of our future work.  

 

Part 1: Presentation Folder

A presentation folder designed to contain information about Harborline Staffing and our company’s capabilities. This folder should be very professional and give the feeling that our company is reliable. Abstract designs are fine; incorporating different areas of science would be nice as well. We are open to colors/designs but the logo colors must not be changed.

We are looking for something simple and not too busy.  If you can incorporate the above that is great, but we are looking for a simple design.

 

Part 2: Folder Inserts

In one of the pockets of the folder we would like to have three sheets of paper. The paper will be displayed in a descending fashion so that you are able to see the 1.5 inch header on the top of each paper. (Full sheet in back, sheet trimmed 1.5 inches, sheet trimmed 3 inches in the front. The top 1.5 inch border is all that will need to be designed; we will trim the sheets after printing.

Target Market(s)

Human Resources professionals and hiring managers of biotech, pharmaceutical, and scientific companies

Requirements
Must have
• Folder:

• - Harborline Staffing Logo Must been on white background
• - Company slogan must be on the cover, “The Chemistry of Hiring”
• Interior
• - Must include space for a business card to be attached on one of the folder flaps
• - The logo and Slogan should also appear on one of the folder interior pocket flaps

• Please use the attached AI format from the company that will be printing out materials There is an outside and inside printing format.

•  

• Inserts:

• - Inserts must have Harborline Staffing Logo on header
• - Insert must have design on the 1.5 inch of the page (Three Pages)
• - Three Sheets must be labeled, Direct Hire, Temporary Staffing, About Harborline Staffing (This text layer must be left editable in the file delivered version for future revisions)

Nice to have
• Pictures or silhouettes of people
• Something incorporating different scientific themes

• Something incorporating several areas of science. Just a few ideas but there are countless areas of science, (Electronics, Medical, Environmental, Pharmaceutical, Biotech, Chemical, Aerospace, Engineering)
Should not have
• We are open to anything that you can think of.  We want to base an entire series of promotional materials on these designs so we are open minded.

```html
<!DOCTYPE html>
<html lang="en">
<head>
<meta charset="utf-8">
<title>Harborline Staffing — Presentation Folder, Inside Spread</title>
<link rel="stylesheet" href="https://fonts.googleapis.com/css2?family=Open+Sans:wght@400;600&display=swap">
<style>
  :root {
    --backdrop: #3c3c3c;
    --folder-light: #e0dfc6;
    --folder-dark: #cbcab4;
    --paper: #ffffff;
    --teal: #9fc2bb;
    --teal-soft: #dbe9e6;
    --logo-green: #1f5a3a;
    --title-ink: #1b1b1b;
    --title-accent: #e0141e;
    --slogan-ink: #555555;
    --coat-light: #f4f6f6;
    --coat-shade: #c9d2d1;
  }
  * { margin: 0; padding: 0; box-sizing: border-box; }
  html, body {
    width: 1200px; height: 848px; overflow: hidden;
    background: var(--backdrop);
    font-family: "Open Sans", Arial, sans-serif;
  }
  .folder {
    position: absolute; left: 170px; top: 112px;
    width: 842px; height: 562px;
    display: flex;
  }
  .folder-panel {
    position: relative; width: 421px; height: 100%;
    background: linear-gradient(90deg, var(--folder-light), var(--folder-dark));
  }
  .folder-panel--right {
    background: linear-gradient(90deg, var(--folder-dark), var(--folder-light) 12%, var(--folder-light));
    border-left: 1px solid #b7b6a0;
  }
  .pocket {
    position: absolute; left: 0; bottom: 0;
    width: 100%; height: 178px;
    background: var(--paper);
    box-shadow: 0 -2px 4px rgba(0,0,0,0.12);
  }
  .brand-name {
    position: absolute;
    font-weight: 400; color: var(--logo-green);
    text-transform: uppercase; letter-spacing: 0.04em;
    white-space: nowrap;
  }
  .pocket .brand-name { left: 18px; top: 26px; font-size: 11px; }
  .slogan {
    position: absolute; right: 16px; bottom: 16px;
    font-size: 10px; letter-spacing: 0.05em; color: var(--slogan-ink);
    white-space: nowrap;
  }
  .insert-stack {
    position: absolute; left: 18px; top: 18px;
    width: 384px; height: 520px;
  }
  .insert-sheet {
    position: absolute; left: 0; right: 0; bottom: 0;
    background: var(--paper);
    box-shadow: 0 1px 3px rgba(0,0,0,0.15);
  }
  .insert-sheet--full { top: 0; }
  .insert-sheet--mid { top: 70px; }
  .insert-sheet--front { top: 140px; }
  .insert-header {
    position: relative; height: 70px;
    background: linear-gradient(180deg, var(--paper) 35%, var(--teal-soft) 65%, var(--teal) 100%);
  }
  .insert-header .brand-name { left: 9px; top: 16px; font-size: 8.5px; }
  .insert-title {
    position: absolute; right: 10px; top: 5px;
    font-size: 18px; font-weight: 400; line-height: 24px; color: var(--title-ink);
    text-shadow: 1px 1px 1px rgba(0,0,0,0.25);
    white-space: nowrap;
  }
  .insert-title .initial { color: var(--title-accent); }
  .coat-row {
    position: absolute; right: 4px; bottom: 3px; height: 36px;
    background: linear-gradient(180deg, var(--coat-light), var(--coat-shade));
    border-radius: 2px; opacity: 0.9;
  }
</style>
</head>
<body>
  <div class="folder">
    <section class="folder-panel folder-panel--left">
      <div class="pocket">
        <span class="brand-name">Harborline Staffing</span>
      </div>
    </section>

    <section class="folder-panel folder-panel--right">
      <div class="insert-stack">
        <div class="insert-sheet insert-sheet--full">
          <header class="insert-header">
            <span class="brand-name">Harborline Staffing</span>
            <div class="coat-row" style="width:84px" role="img" aria-label="White lab coats on hangers"></div>
            <h2 class="insert-title"><span class="initial">D</span>irect <span class="initial">H</span>ire</h2>
          </header>
        </div>
        <div class="insert-sheet insert-sheet--mid">
          <header class="insert-header">
            <span class="brand-name">Harborline Staffing</span>
            <div class="coat-row" style="width:170px" role="img" aria-label="Row of white lab coats on hangers"></div>
            <h2 class="insert-title"><span class="initial">T</span>emporary <span class="initial">S</span>taffing</h2>
          </header>
        </div>
        <div class="insert-sheet insert-sheet--front">
          <header class="insert-header">
            <span class="brand-name">Harborline Staffing</span>
            <div class="coat-row" style="width:232px" role="img" aria-label="Groups of white lab coats on hangers"></div>
            <h2 class="insert-title"><span class="initial">A</span>bout <span class="initial">H</span>arborline <span class="initial">S</span>taffing</h2>
          </header>
        </div>
      </div>
      <div class="pocket">
        <p class="slogan">The Chemistry of Hiring</p>
      </div>
    </section>
  </div>
</body>
</html>
```